Web design for a dental and eye clinic

We need a web design for a dental and eye clinic ( with medical laboratory services) with two branches in Lagos Nigeria. The ultimate aim is to attract more patronage. The design should have links to social media and should have provision for appointments and enquiries. Blue should be part of the colours

Name of facility. VORANTECLINICS Added Saturday, May 27, 2017

Target Market(s)

Lagos. Nigeria

Industry/Entity Type

Health Care

Number of Pages Required

3 page

Font styles to use
Sans Serif

Colors
85cae6
cadf82

Requirements
Must have
• a projection of the professioal services rendered
Nice to have
• portal for enquiries and appointments
• Link to our facebook, twitter and instagram

```html
<!DOCTYPE html>
<html lang="en">
<head>
<meta charset="utf-8">
<title>Vorante Clinics – Dental and eye clinic</title>
<link href="https://fonts.googleapis.com/css2?family=Quicksand:wght@400;500;600;700&family=Lato:wght@400;700&display=swap" rel="stylesheet">
<style>
:root{
  --navy:#2c3592;
  --blue:#1c8fd8;
  --sky:#85cae6;
  --line:#d9dde4;
  --text:#333a45;
  --muted:#6b7280;
  --field:#55b9e6;
  --band:#f4f4f5;
  --white:#ffffff;
}
*{box-sizing:border-box;margin:0;padding:0}
html,body{width:1200px;height:2956px;overflow:hidden}
body{position:relative;background:var(--white);font-family:"Lato",sans-serif;color:var(--text)}
.abs{position:absolute}
.heading{font-family:"Quicksand",sans-serif}

/* top bar */
.contact-top{left:120px;top:36px;width:220px;text-align:right;font-size:12.5px;line-height:22px;font-weight:700;color:#222}
.icon-box{width:34px;height:34px;border:1px solid var(--line);border-radius:3px;display:flex;align-items:center;justify-content:center}
.brand{left:520px;top:22px;display:flex;align-items:center;gap:10px}
.brand-dot{width:42px;height:42px;border-radius:50%;background:var(--blue)}
.brand-name{font-family:"Quicksand",sans-serif;font-weight:700;font-size:26px;color:var(--navy);line-height:1}
.hours{left:850px;top:36px;font-size:12.5px;line-height:22px;font-weight:700;color:#222}

/* nav */
.nav{left:0;top:122px;width:1200px;height:42px;border-top:1px solid var(--line);border-bottom:1px solid var(--line)}
.nav-item{top:12px;font-family:"Quicksand",sans-serif;font-size:13.5px;color:#333}
.nav-item::before{content:"";position:absolute;left:-22px;top:6px;width:5px;height:5px;border-radius:50%;background:#999}
.nav-item.active{color:var(--navy)}
.nav-item.active::before{background:var(--navy)}
.social{top:9px;width:24px;height:24px;border-radius:50%}

/* hero */
.hero{left:0;top:164px;width:1200px;height:498px;background:linear-gradient(100deg,#9fd8f0 0%,#86c9ec 40%,#8fa8e0 75%,#9a90d6 100%)}
.hero-photo{left:0;top:0;width:720px;height:498px;background:linear-gradient(90deg,rgba(235,215,225,.55),rgba(200,200,235,.25) 60%,rgba(150,170,230,0))}
.hero-title{right:54px;top:160px;font-family:"Quicksand",sans-serif;font-weight:500;font-size:54px;color:var(--white);letter-spacing:1px}
.hero-sub{right:58px;top:236px;font-family:"Quicksand",sans-serif;font-size:22px;color:var(--white)}
.hero-btn{left:954px;top:304px;width:186px;height:46px;background:var(--white);font-size:14px;color:#222;display:flex;align-items:center;justify-content:center;font-weight:700}

/* services strip */
.services{left:0;top:662px;width:1200px;height:160px;border-bottom:1px solid var(--line)}
.service{top:0;width:282px;height:160px;border-right:1px solid var(--line);text-align:center}
.service svg{margin-top:24px}
.service-name{position:absolute;left:0;right:0;top:112px;font-family:"Quicksand",sans-serif;font-size:19px;color:var(--navy)}

/* laboratory */
.lab-frame{left:83px;top:948px;width:552px;height:374px;border:1.5px solid #888}
.lab-photo{left:63px;top:928px;width:554px;height:374px;background:linear-gradient(135deg,#e6e4e6,#c7c9cf 55%,#9ea3ad)}
.lab-title{left:688px;top:916px;font-size:34px;font-weight:600;color:var(--navy)}
.lab-title span{color:var(--blue)}
.lab-text{left:688px;top:990px;width:470px;font-size:14.5px;line-height:29px;color:#222}
.lab-list{left:692px;top:1144px;list-style:none;font-size:14px;color:#222}
.lab-list li{height:34px;position:relative;padding-left:20px}
.lab-list li::before{content:"";position:absolute;left:0;top:7px;width:6px;height:6px;border-radius:50%;background:var(--navy)}
.btn{background:linear-gradient(180deg,var(--blue),#1a5fb8);color:var(--white);font-weight:700;display:flex;align-items:center;justify-content:center}
.lab-btn{left:695px;top:1267px;width:243px;height:45px;font-size:14px}

/* appointment */
.appointment{left:0;top:1370px;width:1200px;height:565px;background:var(--band)}
.appt-title{left:0;width:1200px;top:1460px;text-align:center;font-size:32px;font-weight:600;color:var(--navy)}
.field{width:454px;height:65px;border:2px solid var(--field);background:var(--band);display:flex;align-items:center;justify-content:space-between;padding:0 26px;font-family:"Quicksand",sans-serif;font-size:17px;color:#888}
.submit{left:536px;top:1797px;width:122px;height:49px;font-size:18px}

/* blog */
.blog-title{left:489px;top:1996px;padding-left:22px;border-left:4px solid var(--navy);font-size:31px;font-weight:500;color:#222;line-height:40px}
.card{top:2108px;width:342px;text-align:center}
.card.featured{background:var(--white);box-shadow:0 6px 22px rgba(0,0,0,.14);height:380px}
.card-photo{width:342px;height:244px}
.card-title{margin-top:28px;font-family:"Quicksand",sans-serif;font-size:22px;color:var(--blue);font-weight:500}
.card-sub{margin-top:18px;font-size:13px;color:#555}
.card-date{margin-top:12px;font-size:13px;color:#555}
.dots{left:572px;top:2536px;display:flex;gap:9px}
.dots span{width:9px;height:9px;border-radius:50%;background:#bbb}
.dots span:first-child{background:var(--blue)}

/* footer */
.footer{left:0;top:2577px;width:1200px;height:339px;background:linear-gradient(180deg,#2d3f9e 0%,#2561c6 60%,#1c7fd8 100%);color:var(--white)}
.f-social{top:63px;width:22px;height:22px;border-radius:50%;background:var(--white)}
.f-nav{top:62px;font-size:14px;letter-spacing:.5px}
.f-rule{left:42px;top:101px;width:1112px;height:1px;background:rgba(255,255,255,.35)}
.f-brand{left:60px;top:134px;display:flex;align-items:center;gap:10px}
.f-brand .brand-dot{background:var(--white);width:38px;height:38px}
.f-brand .brand-name{color:var(--white);font-size:24px}
.f-tag{left:60px;top:268px;font-size:11px}
.f-div{top:128px;width:1px;height:190px;background:rgba(255,255,255,.45)}
.f-links{left:470px;top:150px;font-size:12.5px;font-weight:700;line-height:34px}
.f-head{font-family:"Quicksand",sans-serif;font-size:20px;font-weight:700;text-align:center}
.f-contact{left:634px;top:134px;width:268px;text-align:center}
.f-contact p{font-size:12.5px;font-weight:700;line-height:26px}
.f-news{left:902px;top:134px;width:298px;text-align:center}
.f-news p{font-size:11px;font-weight:700;line-height:20px;margin-top:12px}
.f-form{left:946px;top:228px;display:flex}
.f-input{width:148px;height:36px;background:var(--white);font-size:11px;color:#999;padding:11px 10px}
.f-send{width:54px;height:36px;background:var(--navy);display:flex;align-items:center;justify-content:center}
.bottom-bar{left:0;top:2916px;width:1200px;height:40px;background:#2e3a9a;color:var(--white);font-size:12px;font-weight:700}
</style>
</head>
<body>

<!-- top bar -->
<div class="abs contact-top">Free Call +1555 0142 907<br>1234 street name, location</div>
<div class="abs icon-box" style="left:366px;top:40px">
  <svg width="18" height="18" viewBox="0 0 24 24"><path d="M6.6 10.8a15 15 0 0 0 6.6 6.6l2.2-2.2a1 1 0 0 1 1-.25 11 11 0 0 0 3.6.6 1 1 0 0 1 1 1V20a1 1 0 0 1-1 1A17 17 0 0 1 3 4a1 1 0 0 1 1-1h3.5a1 1 0 0 1 1 1 11 11 0 0 0 .6 3.6 1 1 0 0 1-.25 1z" fill="#1c8fd8"/></svg>
</div>
<div class="abs brand"><div class="brand-dot"></div><div class="brand-name">Vorante<br>Clinics</div></div>
<div class="abs" style="left:798px;top:40px">
  <svg width="28" height="28" viewBox="0 0 24 24" fill="none" stroke="#1c8fd8" stroke-width="1.5"><rect x="3" y="5" width="18" height="16" rx="2"/><path d="M3 10h18M8 3v4M16 3v4"/></svg>
</div>
<div class="abs hours">Open hours:<br>Mn - St: 8:00am - 9:00pm Sn: Closed</div>

<!-- nav -->
<nav class="abs nav">
  <span class="abs nav-item active" style="left:80px">Home</span>
  <span class="abs nav-item" style="left:204px">About us</span>
  <span class="abs nav-item" style="left:348px">Services</span>
  <span class="abs nav-item" style="left:490px">Doctors</span>
  <span class="abs nav-item" style="left:628px">Blog</span>
  <span class="abs nav-item" style="left:740px">Contact us</span>
  <svg class="abs" style="left:938px;top:11px" width="20" height="20" viewBox="0 0 24 24" fill="none" stroke="#1c8fd8" stroke-width="2.5"><circle cx="10" cy="10" r="7"/><path d="M15 15l6 6"/></svg>
  <div class="abs" style="left:984px;top:6px;width:1px;height:30px;background:#999"></div>
  <div class="abs social" style="left:1013px;background:#2c4fa0"></div>
  <div class="abs social" style="left:1061px;background:#e0533d"></div>
  <div class="abs social" style="left:1109px;background:#3ab0e8"></div>
</nav>

<!-- hero -->
<section class="abs hero">
  <div class="abs hero-photo" role="img" aria-label="Close-up of a smiling woman with white teeth"></div>
  <h1 class="abs hero-title">Dental and eye clinic</h1>
  <p class="abs hero-sub">( with medical laboratory services)</p>
  <div class="abs hero-btn">Make an appoinment</div>
</section>

<!-- services -->
<section class="abs services">
  <svg class="abs" style="left:24px;top:68px" width="18" height="22" viewBox="0 0 18 22"><path d="M13 2L4 11l9 9" fill="none" stroke="#777" stroke-width="3"/></svg>
  <svg class="abs" style="left:1158px;top:68px" width="18" height="22" viewBox="0 0 18 22"><path d="M5 2l9 9-9 9" fill="none" stroke="#777" stroke-width="3"/></svg>
  <div class="abs service" style="left:52px">
    <svg width="60" height="70" viewBox="0 0 60 70" fill="none" stroke="#2c3592" stroke-width="2.5"><path d="M16 12c-8 0-12 7-11 16 1 8 4 12 5 20 1 7 2 14 6 14s4-12 8-12 4 12 8 12 5-7 6-14c1-8 4-12 5-20 1-9-3-16-11-16-4 0-6 2-8 2s-4-2-8-2z"/><path d="M52 2v10M47 7h10" stroke="#1c8fd8"/></svg>
    <div class="service-name">Teeth whitening</div>
  </div>
  <div class="abs service" style="left:334px">
    <svg width="60" height="70" viewBox="0 0 60 70" fill="none" stroke="#2c3592" stroke-width="2.5"><path d="M10 10c0-4 6-6 20-6s20 2 20 6-6 8-20 8-20-4-20-8z"/><path d="M18 22h24M20 30h20M22 38h16M24 46h12M27 54h6M30 18v46"/></svg>
    <div class="service-name">Dental implantation</div>
  </div>
  <div class="abs service" style="left:616px">
    <svg width="70" height="70" viewBox="0 0 70 70" fill="none" stroke="#2c3592" stroke-width="2.5"><circle cx="30" cy="28" r="22"/><path d="M16 28c6-8 22-8 28 0-6 8-22 8-28 0z"/><circle cx="30" cy="28" r="4" fill="#1c8fd8"/><path d="M46 44l16 16"/></svg>
    <div class="service-name">Eye test</div>
  </div>
  <div class="abs service" style="left:898px;border-right:none">
    <svg width="80" height="70" viewBox="0 0 80 70" fill="none" stroke="#2c3592" stroke-width="2.5"><path d="M6 38c18-22 50-22 68 0-18 22-50 22-68 0z"/><circle cx="40" cy="38" r="11"/><circle cx="40" cy="38" r="5" fill="#2c3592"/><path d="M54 20l16-16" stroke="#1c8fd8"/></svg>
    <div class="service-name">Eye infection care</div>
  </div>
</section>

<!-- laboratory -->
<div class="abs lab-frame"></div>
<div class="abs lab-photo" role="img" aria-label="Laboratory technician in gloves loading test tubes into a centrifuge"></div>
<h2 class="abs lab-title heading">Vorante Laboratory <span>services</span></h2>
<p class="abs lab-text">Lorem Ipsum is simply dummy text of the printing and typesetting industry. Lorem Ipsum has been the industry's standard dummy text ever since the 1500s, when an unknown printer took a galley</p>
<ul class="abs lab-list">
  <li>Certified Doctors</li>
  <li>Latest Technology Equipment</li>
  <li>Insurance facility available</li>
</ul>
<div class="abs btn lab-btn">Get laboratory service now</div>

<!-- appointment -->
<section class="abs appointment"></section>
<svg class="abs" style="left:0;top:1370px" width="1200" height="50"><path d="M0 48L1200 6" stroke="#1c8fd8" stroke-width="4"/><path d="M0 48L1200 6V0H0z" fill="#fff"/></svg>
<svg class="abs" style="left:0;top:1900px" width="1200" height="40"><path d="M0 6L1200 34" stroke="#1a6fd0" stroke-width="4"/><path d="M0 6L1200 34V40H0z" fill="#fff"/></svg>
<h2 class="abs appt-title heading">Make an appoinment</h2>
<div class="abs field" style="left:130px;top:1568px">Name
  <svg width="20" height="20" viewBox="0 0 24 24" fill="#999"><circle cx="12" cy="7" r="5"/><path d="M2 23c0-6 4-9 10-9s10 3 10 9z"/></svg></div>
<div class="abs field" style="left:628px;top:1568px">Email Id
  <svg width="30" height="20" viewBox="0 0 30 20"><rect width="30" height="20" fill="#999"/><path d="M0 0l15 11L30 0" fill="none" stroke="#f4f4f5" stroke-width="2"/></svg></div>
<div class="abs field" style="left:130px;top:1661px">Phone number
  <svg width="18" height="18" viewBox="0 0 24 24"><path d="M6.6 10.8a15 15 0 0 0 6.6 6.6l2.2-2.2a1 1 0 0 1 1-.25 11 11 0 0 0 3.6.6 1 1 0 0 1 1 1V20a1 1 0 0 1-1 1A17 17 0 0 1 3 4a1 1 0 0 1 1-1h3.5a1 1 0 0 1 1 1 11 11 0 0 0 .6 3.6 1 1 0 0 1-.25 1z" fill="#999"/></svg></div>
<div class="abs field" style="left:628px;top:1661px">Choose Date and time
  <svg width="20" height="20" viewBox="0 0 24 24" fill="none" stroke="#999" stroke-width="2"><rect x="3" y="5" width="18" height="16" rx="2"/><path d="M3 10h18M8 3v4M16 3v4"/></svg></div>
<div class="abs btn submit">Submit</div>

<!-- blog -->
<h2 class="abs blog-title heading">Latest blog</h2>
<article class="abs card" style="left:43px">
  <div class="card-photo" role="img" aria-label="Dental treatment chair and equipment in a bright clinic room" style="background:linear-gradient(135deg,#f2f2f2,#bfc2c6 60%,#6f7378)"></div>
  <h3 class="card-title">Lorem ipsum</h3>
  <p class="card-sub">lorem ipsum</p>
  <p class="card-date">March 20 – April 2, 2017</p>
</article>
<article class="abs card featured" style="left:429px">
  <div class="card-photo" role="img" aria-label="Doctor in a white coat with a stethoscope and pens in the pocket" style="background:linear-gradient(90deg,#d9b48c,#efe9e2 50%,#d8d4cf)"></div>
  <h3 class="card-title">Lorem ipsum</h3>
  <p class="card-sub">lorem ipsum</p>
  <p class="card-date">March 20 – April 2, 2017</p>
</article>
<article class="abs card" style="left:812px">
  <div class="card-photo" role="img" aria-label="Doctor in blue scrubs looking thoughtful" style="background:linear-gradient(135deg,#6fb3e0,#2e6fa8 55%,#1d3f66)"></div>
  <h3 class="card-title">Lorem ipsum</h3>
  <p class="card-sub">lorem ipsum</p>
  <p class="card-date">March 20 – April 2, 2017</p>
</article>
<div class="abs dots"><span></span><span></span><span></span></div>

<!-- footer -->
<footer class="abs footer">
  <div class="abs f-social" style="left:60px;opacity:.9"></div>
  <div class="abs f-social" style="left:108px;background:#e0533d"></div>
  <div class="abs f-social" style="left:156px;background:#3ab0e8"></div>
  <span class="abs f-nav" style="left:470px">HOME</span>
  <span class="abs f-nav" style="left:600px">ABOUT US</span>
  <span class="abs f-nav" style="left:756px">SERVICES</span>
  <span class="abs f-nav" style="left:902px">BLOG</span>
  <span class="abs f-nav" style="left:1022px">CONTACTUS</span>
  <div class="abs f-rule"></div>
  <div class="abs f-brand"><div class="brand-dot"></div><div class="brand-name">Vorante<br>Clinics</div></div>
  <p class="abs f-tag">Dental and eye clinic with medical laborary services</p>
  <div class="abs f-div" style="left:408px"></div>
  <div class="abs f-links">Log in<br>Insurance<br>Pay online<br>book appoinmnet</div>
  <div class="abs f-div" style="left:634px"></div>
  <div class="abs f-contact">
    <div class="f-head">Contact us</div>
    <p style="margin-top:12px">123456789<br>1234 tsteert name<br>location<br>info@vorante.com</p>
  </div>
  <div class="abs f-div" style="left:902px"></div>
  <div class="abs f-news">
    <div class="f-head">Newsletter</div>
    <p>subcribe here to know more<br>about services we offer</p>
  </div>
  <div class="abs f-form">
    <div class="f-input">email id</div>
    <div class="f-send"><svg width="24" height="22" viewBox="0 0 24 22"><path d="M0 10L24 0 18 22 11 14z" fill="#fff"/></svg></div>
  </div>
</footer>
<div class="abs bottom-bar">
  <span class="abs" style="left:60px;top:13px">Copyright 2017All Rights Reserved.</span>
  <span class="abs" style="left:900px;top:13px">Terms &amp; Conditions &nbsp;&nbsp;&nbsp;|</span>
  <span class="abs" style="left:1068px;top:13px">Privacy Policy</span>
</div>

</body>
</html>
```